North American Image Consultant needs a process design and a method design

I am an Image/style consultant who works with business professionals in the Toronto area. My product name is called " S.H.A.R.E." I help people understand how your " Style, Habits, Attitude, Reach and Energy. I help people create a professional appearance in a business casual/digital world, from head to toe. I work with them through all 4 seasons, to achieve consistency and confidence to help them look and feel amazing, inside and out.. easily and effortlessly. My main colour is aqua blue, I don't want any neon or primary colours. I would like it to appeal to both men and women ( but mostly women)
The final design should be an easy to follow path to success with an understanding of what S.H.A.R.E will do for them.

Target Market(s)

mid level executive business professionals 38-58 yrs old they want to look and feel amazing inside and out. They want to up their game, get the promotion, nail the interview , and feel they're relevant and taken seriously in a leadership way.

Font styles to use
Serif

Colors
b7a5cd
886aae
85cae6
33a6d7
33b8a4
f04a50
00a990
e34297
85acd3

Requirements
Must have
• A classy, casual feel. A positive feel good feeling
Nice to have
• A 3 colour balance ( Not black based)
Should not have
• Too many squares
too many squiggly lines.
Not too masculine/feminine
too childish/youthful
Not office focused or bank focused

```html
<!DOCTYPE html>
<html lang="en">
<head>
<meta charset="utf-8">
<title>Maintaining a Professional Appearance – S.H.A.R.E.</title>
<link rel="stylesheet" href="https://fonts.googleapis.com/css2?family=Libre+Caslon+Text:wght@400;700&family=EB+Garamond:wght@400;500&display=swap">
<style>
  :root{
    --ink:#3b4667;
    --ink-dark:#2c3350;
    --rule:#3b4667;
    --lilac:#b7a5cd;
    --violet:#886aae;
    --sky:#85cae6;
    --ocean:#33a6d7;
    --coral:#f04a50;
    --blush:#f58b8b;
    --teal:#00a990;
    --mint:#33b8a4;
    --steel:#85acd3;
    --navy-blue:#3a6db0;
    --arc:#b9c8cc;
    --dash:#b3b3b3;
  }
  *{margin:0;padding:0;box-sizing:border-box}
  html,body{width:1200px;height:927px;overflow:hidden}
  body{background:#fff}
  .canvas{
    position:relative;width:1200px;height:927px;overflow:hidden;
    background:linear-gradient(90deg,#fafafa 0%,#f1f1f1 55%,#e4e4e4 100%);
    font-family:"EB Garamond",serif;color:var(--ink);
  }
  .title{position:absolute;left:61px;top:32px;font-family:"Libre Caslon Text",serif;color:var(--ink)}
  .title-main{font-size:31px;font-weight:700;letter-spacing:.5px;line-height:1.1;text-transform:uppercase}
  .title-sub{font-size:27px;font-weight:400;line-height:1.2;text-transform:uppercase;margin-top:2px}
  .rule{position:absolute;height:2px;background:var(--rule)}
  .rule-top{left:504px;top:93px;width:636px}
  .rule-bottom{left:62px;top:892px;width:1078px;height:1.5px}

  .intro{position:absolute;left:75px;top:230px;width:229px;font-size:13.2px;line-height:18.2px;text-align:justify;hyphens:auto;color:var(--ink-dark)}
  .intro p{margin-bottom:17px}

  .diagram{position:absolute;left:0;top:0;width:1200px;height:927px}

  .hub{position:absolute;left:349px;top:353px;width:270px;height:270px;border-radius:50%;
    background:linear-gradient(145deg,#f4f4f4,#e6e6e6);
    box-shadow:0 8px 18px rgba(0,0,0,.12),inset 0 2px 3px #fff}
  .hub-face{position:absolute;left:13px;top:13px;width:244px;height:244px;border-radius:50%;
    background:radial-gradient(circle at 40% 35%,#ffffff 0%,#f2f2f2 60%,#e9e9e9 100%);
    box-shadow:0 2px 6px rgba(0,0,0,.1);display:flex;align-items:center;justify-content:center}
  .hub-word{font-family:"EB Garamond",serif;font-size:56px;letter-spacing:1px;color:var(--ink)}

  .step{position:absolute;width:412px;height:120px}
  .step svg{position:absolute;left:0;top:0;filter:drop-shadow(0 5px 6px rgba(0,0,0,.18))}
  .step-letter{position:absolute;left:22px;top:0;width:80px;height:120px;display:flex;align-items:center;justify-content:center;
    font-family:"Libre Caslon Text",serif;font-size:62px;color:#fff}
  .step-name{position:absolute;left:145px;top:24px;font-family:"Libre Caslon Text",serif;font-weight:700;font-size:23px;color:#fff;text-transform:uppercase}
  .step-note{position:absolute;left:145px;top:59px;font-size:19px;line-height:25px;color:var(--ink-dark)}
  .step-style{left:622px;top:134px}
  .step-habits{left:692px;top:278px}
  .step-habits .step-letter{color:var(--ink)}
  .step-habits .step-name{color:var(--ink)}
  .step-attitude{left:754px;top:429px}
  .step-attitude .step-name{top:14px}
  .step-attitude .step-note{top:47px}
  .step-reach{left:692px;top:578px}
  .step-energy{left:622px;top:723px}
</style>
</head>
<body>
<main class="canvas">
  <header class="title">
    <h1 class="title-main">Maintaining a Professional Appearance</h1>
    <h2 class="title-sub">In a Business Casual World</h2>
  </header>
  <div class="rule rule-top"></div>

  <section class="intro">
    <p>Lorem ipsum dolor sit amet, consectetuer adipiscing elit, sed diam nonummy nibh euismod tincidunt ut laoreet dolore magna aliquam erat volutpat. Ut wisi enim ad minim veniam, quis nostrud exerci tation ullamcorper suscipit lobortis nisl ut aliquip ex ea commodo consequat. Duis autem vel eum iriure dolor in hendrerit in vulputate velit esse molestie consequat.</p>
    <p>Lorem ipsum dolor sit amet, consectetuer adipiscing elit, sed diam nonummy nibh euismod tincidunt ut laoreet dolore magna aliquam erat volutpat.</p>
    <p>Ut wisi enim ad minim veniam, quis nostrud exerci tation ullamcorper suscipit lobortis nisl ut aliquip ex ea commodo consequat. Duis autem vel eum iriure dolor in hendrerit in vulputate velit esse molestie consequat.</p>
    <p>Lorem ipsum dolor dolore eu feugiat nulla facilisis at vero eros et accumsan et iusto odio dignissim qui blandit praesent.</p>
  </section>

  <svg class="diagram" width="1200" height="927" viewBox="0 0 1200 927" aria-hidden="true">
    <defs>
      <linearGradient id="dot-mix" x1="0" y1="0" x2="1" y2="0">
        <stop offset="0.5" stop-color="#e0a13a"/><stop offset="0.5" stop-color="#33a6d7"/>
      </linearGradient>
    </defs>
    <path d="M492 260 A228 228 0 0 1 492 716" fill="none" stroke="var(--dash)" stroke-width="2" stroke-dasharray="3 4"/>
    <path d="M490 312 A180 180 0 0 1 490 664" fill="none" stroke="var(--arc)" stroke-width="9" stroke-linecap="butt"/>
    <g fill="none" stroke="#b9c4c8" stroke-width="1.2">
      <polyline points="565,306 590,234 638,234"/>
      <polyline points="640,362 656,350 680,338"/>
      <polyline points="678,488 744,488"/>
      <polyline points="640,610 656,622 680,640"/>
      <polyline points="565,670 590,745 640,745"/>
    </g>
    <g fill="#b9c4c8">
      <circle cx="638" cy="234" r="2.5"/><circle cx="680" cy="338" r="2.5"/><circle cx="744" cy="488" r="2.5"/>
      <circle cx="680" cy="640" r="2.5"/><circle cx="640" cy="745" r="2.5"/>
      <circle cx="565" cy="306" r="2.5"/><circle cx="565" cy="670" r="2.5"/>
    </g>
    <g stroke="#fff" stroke-width="5" style="filter:drop-shadow(0 2px 3px rgba(0,0,0,.2))">
      <circle cx="558" cy="326" r="10" fill="var(--violet)"/>
      <circle cx="628" cy="380" r="10" fill="url(#dot-mix)"/>
      <circle cx="664" cy="488" r="10" fill="var(--coral)"/>
      <circle cx="628" cy="594" r="10" fill="var(--teal)"/>
      <circle cx="558" cy="650" r="10" fill="var(--navy-blue)"/>
    </g>
  </svg>

  <div class="hub"><div class="hub-face"><span class="hub-word">SHARE</span></div></div>

  <article class="step step-style">
    <svg width="412" height="120" viewBox="0 0 412 120">
      <defs>
        <linearGradient id="g-style" x1="0" x2="1"><stop offset="0" stop-color="var(--lilac)"/><stop offset="1" stop-color="var(--violet)"/></linearGradient>
        <linearGradient id="d-style" x1="0" y1="0" x2="1" y2="1"><stop offset="0" stop-color="#b29fcf"/><stop offset="1" stop-color="#7d5fa6"/></linearGradient>
      </defs>
      <polygon points="0,60 50,0 362,0 412,60 362,120 50,120" fill="url(#g-style)"/>
      <polygon points="2,60 62,0 122,60 62,120" fill="url(#d-style)"/>
    </svg>
    <span class="step-letter">S</span>
    <h3 class="step-name">Style</h3>
    <p class="step-note">Your signature look</p>
  </article>

  <article class="step step-habits">
    <svg width="412" height="120" viewBox="0 0 412 120">
      <defs>
        <linearGradient id="g-habits" x1="0" x2="1"><stop offset="0" stop-color="var(--sky)"/><stop offset="1" stop-color="var(--ocean)"/></linearGradient>
        <linearGradient id="d-habits" x1="0" y1="0" x2="1" y2="1"><stop offset="0" stop-color="#9ad5ee"/><stop offset="1" stop-color="#3aa2d2"/></linearGradient>
      </defs>
      <polygon points="0,60 50,0 362,0 412,60 362,120 50,120" fill="url(#g-habits)"/>
      <polygon points="2,60 62,0 122,60 62,120" fill="url(#d-habits)"/>
    </svg>
    <span class="step-letter">H</span>
    <h3 class="step-name">Habits</h3>
    <p class="step-note">Routines that last all year</p>
  </article>

  <article class="step step-attitude">
    <svg width="412" height="120" viewBox="0 0 412 120">
      <defs>
        <linearGradient id="g-attitude" x1="0" x2="1"><stop offset="0" stop-color="var(--coral)"/><stop offset="1" stop-color="var(--blush)"/></linearGradient>
        <linearGradient id="d-attitude" x1="0" y1="0" x2="1" y2="1"><stop offset="0" stop-color="#f58a8c"/><stop offset="1" stop-color="#e0434a"/></linearGradient>
      </defs>
      <polygon points="0,60 50,0 362,0 412,60 362,120 50,120" fill="url(#g-attitude)"/>
      <polygon points="2,60 62,0 122,60 62,120" fill="url(#d-attitude)"/>
    </svg>
    <span class="step-letter">A</span>
    <h3 class="step-name">Attitude</h3>
    <p class="step-note">The ‘Sound,’ of your presence<br>when you walk into a room</p>
  </article>

  <article class="step step-reach">
    <svg width="412" height="120" viewBox="0 0 412 120">
      <defs>
        <linearGradient id="g-reach" x1="0" x2="1"><stop offset="0" stop-color="var(--teal)"/><stop offset="1" stop-color="var(--mint)"/></linearGradient>
        <linearGradient id="d-reach" x1="0" y1="0" x2="1" y2="1"><stop offset="0" stop-color="#0b9c86"/><stop offset="1" stop-color="#0a8f7b"/></linearGradient>
      </defs>
      <polygon points="0,60 50,0 362,0 412,60 362,120 50,120" fill="url(#g-reach)"/>
      <polygon points="2,60 62,0 122,60 62,120" fill="url(#d-reach)"/>
    </svg>
    <span class="step-letter">R</span>
    <h3 class="step-name">Reach</h3>
    <p class="step-note">Extend your influence further</p>
  </article>

  <article class="step step-energy">
    <svg width="412" height="120" viewBox="0 0 412 120">
      <defs>
        <linearGradient id="g-energy" x1="0" x2="1"><stop offset="0" stop-color="var(--steel)"/><stop offset="1" stop-color="var(--navy-blue)"/></linearGradient>
        <linearGradient id="d-energy" x1="0" y1="0" x2="1" y2="1"><stop offset="0" stop-color="#6f9ed3"/><stop offset="1" stop-color="#3466ab"/></linearGradient>
      </defs>
      <polygon points="0,60 50,0 362,0 412,60 362,120 50,120" fill="url(#g-energy)"/>
      <polygon points="2,60 62,0 122,60 62,120" fill="url(#d-energy)"/>
    </svg>
    <span class="step-letter">E</span>
    <h3 class="step-name">Energy</h3>
    <p class="step-note">Look and feel amazing</p>
  </article>

  <div class="rule rule-bottom"></div>
</main>
</body>
</html>
```